Dishcart

App Design for a an application on which you can order take aways from restaurants close to you.
(similar app : https://appvault.example/lu/app/brunomeal-pizza-burger-sushi/id538216047?l=en&mt=8 )

Logo is a taxi (psd of taxi an font attached)

Attached a draft mockup showing the screens needed.

Screens needed :

1. Splash Screen
2. Select you restaurant screen
3. Select your dish (meat, pizza, pasta....)
4. Select your extras (exta cheese, garlik etc...)
5. Exit screen with total amount and confirmation
6. Subscribe Screen where people have to register the first time.

Target Market(s)

age 14-54

Industry/Entity Type

Restaurant

Requirements
Must have
• Wood elements

```html
<!DOCTYPE html>
<html lang="en">
<head>
<meta charset="utf-8">
<title>Dishcart – App</title>
<link href="https://fonts.googleapis.com/css2?family=Russo+One&family=Roboto:wght@400;700&family=Raleway:wght@300;400&display=swap" rel="stylesheet">
<style>
  :root{
    --sky-top:#7fd3e8;
    --sky-bottom:#1b9cc8;
    --ink-white:#ffffff;
    --ink-soft:rgba(255,255,255,.82);
    --line-soft:rgba(255,255,255,.55);
    --screen-black:#0d0d0d;
    --taxi-yellow:#f2ec1a;
    --wood-light:#c89a5e;
    --wood-dark:#7a5430;
    --card-cream:#f7f4e6;
    --night-dark:#1d1a1c;
    --night-amber:#b8622a;
    --field-fill:rgba(255,255,255,.22);
  }
  *{box-sizing:border-box;margin:0;padding:0}
  html,body{width:1200px;height:755px;overflow:hidden}
  body{
    position:relative;
    background:radial-gradient(ellipse at 35% 20%,var(--sky-top) 0%,#41b6dc 45%,var(--sky-bottom) 100%);
    font-family:"Roboto",Arial,sans-serif;color:var(--ink-white);
  }

  /* ---------- titles & notes ---------- */
  .app-title{
    position:absolute;left:48px;top:56px;
    font-family:"Russo One",Arial,sans-serif;font-size:40px;letter-spacing:1px;
    text-shadow:0 3px 0 rgba(0,0,0,.18);
  }
  .note{position:absolute;width:250px}
  .note h2{font-family:"Russo One",Arial,sans-serif;font-size:19px;font-weight:400;margin-bottom:10px;letter-spacing:.5px}
  .note h3{font-family:"Russo One",Arial,sans-serif;font-size:11px;font-weight:400;margin:10px 0 4px}
  .note p{font-size:11px;line-height:1.4;color:var(--ink-soft)}
  .note--places{left:60px;top:470px;width:270px}
  .note--places p{font-size:13px}
  .note--register{left:955px;top:120px;width:215px}
  .note--how{left:955px;top:520px;width:215px}
  .note--how h2{font-size:15px}
  .note--how p{font-size:10px}

  .corner{position:absolute;width:16px;height:16px;border-color:var(--line-soft);border-style:solid;border-width:0}
  .corner--tl{left:-14px;top:-12px;border-top-width:2px;border-left-width:2px}
  .corner--br{right:-14px;bottom:-12px;border-bottom-width:2px;border-right-width:2px}

  .connector{position:absolute;height:1px;background:var(--line-soft);transform-origin:left center}

  /* ---------- screens ---------- */
  .screen{
    position:absolute;top:110px;width:280px;height:498px;
    background:var(--screen-black);overflow:hidden;
    box-shadow:0 18px 40px rgba(0,40,70,.35);
  }
  .screen--places{left:340px}
  .screen--register{left:650px}

  .status-bar{
    height:14px;display:flex;justify-content:space-between;align-items:center;
    padding:0 6px;font-size:8px;background:#000;color:#ddd;position:relative;z-index:2
  }

  /* list of places */
  .wood-backdrop{position:absolute;inset:14px 0 0 0;background:linear-gradient(160deg,var(--wood-light),var(--wood-dark))}
  .places-header{position:relative;background:var(--taxi-yellow);padding:8px 10px;z-index:1}
  .search-field{background:#fff;border-radius:4px;height:24px;display:flex;align-items:center;padding:0 8px;font-size:11px;color:#888;gap:6px}
  .place-list{position:relative;padding:10px;display:flex;flex-direction:column;gap:10px}
  .place-card{
    display:flex;gap:8px;align-items:center;background:var(--card-cream);
    border:3px solid var(--taxi-yellow);padding:6px;height:76px
  }
  .place-photo{width:62px;height:58px;background:linear-gradient(135deg,#c9803d,#5a3a22);flex:none}
  .place-name{font-weight:700;font-size:13px;color:#2a2a2a}
  .place-price{font-size:12px;color:#3a8a2a;font-weight:700;margin-top:4px}

  /* register */
  .night-backdrop{
    position:absolute;inset:14px 0 0 0;
    background:linear-gradient(180deg,var(--night-dark) 0%,#3a2a26 38%,var(--night-amber) 75%,#4a2a18 100%)
  }
  .register-content{position:relative;z-index:1;display:flex;flex-direction:column;align-items:center;padding-top:78px}
  .brand{display:flex;align-items:center;gap:8px;font-family:"Russo One",Arial,sans-serif;font-size:26px}
  .brand-dot{width:12px;height:12px;border-radius:50%;background:var(--ink-white)}
  .register-title{font-family:"Raleway",Arial,sans-serif;font-weight:300;font-size:28px;margin:40px 0 28px}
  .field{
    width:220px;height:34px;margin-bottom:12px;background:var(--field-fill);
    border:1px solid rgba(255,255,255,.4);padding:0 12px;display:flex;align-items:center;
    font-family:"Raleway",Arial,sans-serif;font-size:13px;color:rgba(255,255,255,.75)
  }
</style>
</head>
<body>

  <h1 class="app-title">DISHCART - APP</h1>

  <!-- list of places screen -->
  <section class="screen screen--places" aria-label="List of places screen">
    <div class="status-bar"><span>NOVA</span><span>4:30 AM</span><span>100%</span></div>
    <div class="wood-backdrop" role="img" aria-label="Wooden table texture background"></div>
    <div class="places-header">
      <div class="search-field">
        <svg width="10" height="10" viewBox="0 0 10 10"><circle cx="4" cy="4" r="3" fill="none" stroke="#888" stroke-width="1.4"/><line x1="6.2" y1="6.2" x2="9" y2="9" stroke="#888" stroke-width="1.4"/></svg>
        Search
      </div>
    </div>
    <div class="place-list">
      <article class="place-card"><div class="place-photo" role="img" aria-label="Restaurant dish photo"></div><div><div class="place-name">Bella Roma</div><div class="place-price">$$</div></div></article>
      <article class="place-card"><div class="place-photo" role="img" aria-label="Pizza photo"></div><div><div class="place-name">Pizza Corner</div><div class="place-price">$</div></div></article>
      <article class="place-card"><div class="place-photo" role="img" aria-label="Noodle dish photo"></div><div><div class="place-name">Green Wok</div><div class="place-price">$$</div></div></article>
      <article class="place-card"><div class="place-photo" role="img" aria-label="Sushi photo"></div><div><div class="place-name">Kyoto Rolls</div><div class="place-price">$$$</div></div></article>
    </div>
  </section>

  <!-- register screen -->
  <section class="screen screen--register" aria-label="Register screen">
    <div class="status-bar"><span>NOVA</span><span>4:30 AM</span><span>100%</span></div>
    <div class="night-backdrop" role="img" aria-label="Blurred evening street with bokeh city lights"></div>
    <div class="register-content">
      <div class="brand"><span class="brand-dot"></span>Dishcart</div>
      <div class="register-title">Register now!</div>
      <div class="field">username</div>
      <div class="field">password</div>
    </div>
  </section>

  <!-- connectors -->
  <div class="connector" style="left:300px;top:520px;width:60px"></div>
  <div class="connector" style="left:880px;top:150px;width:70px"></div>
  <div class="connector" style="left:880px;top:540px;width:70px"></div>

  <!-- notes -->
  <aside class="note note--places">
    <span class="corner corner--tl"></span><span class="corner corner--br"></span>
    <h2>LIST OF PLACES</h2>
    <p>In this screen you will be able to seek for your favourite restaurant and proceed to your request. Payment options are displayed for each stablishment and you can add extras to request. Discounts are also possible, depending of your choice</p>
  </aside>

  <aside class="note note--register">
    <span class="corner corner--tl"></span><span class="corner corner--br"></span>
    <h2>REGISTER SCREEN</h2>
    <h3>REGISTER</h3>
    <p>Possibility to make your registration or log into your account on the right top button inside the yellow tab.</p>
    <h3>TERMS&amp;CONDITIONS</h3>
    <p>To live all the experience of the new Dishcart app you will need to agree with terms and conditions in order to avoid future problems with your requests, payments and refunds.</p>
  </aside>

  <aside class="note note--how">
    <span class="corner corner--tl"></span><span class="corner corner--br"></span>
    <h2>HOW TO MAKE YOUR REGISTRATION</h2>
    <p>Screen to proceed to your registration in our database with the common steps: email and password. You will then receive an email to confirm your data. NOW MAKE YOUR SEARCH AND REQUEST!</p>
  </aside>

</body>
</html>
```